Catchy Cards for Hospital

I run a rural hospital in Texas called Pelham Ridge Hospital and am in need of contemporary business cards for all of my Department Heads. While our logo is somewhat simplistic, I don't have the option of changing it at this time, so anything to make the rest of the card present the appearance of a modern, professional healthcare facility would be great. Although the attached files are in black, our hospital colors are in a copper brown and black. I need to be able to change the name and title on the card so I can get cards printed for various department heads.

Target Market(s)

Referring physicians, large hospital systems, national organizations, state and federal government

Industry/Entity Type

Hospital

Contact Information for Business Card

Name Derek Solano
Title CEO

Phone: Main 325-740-2386 & Direct xxxxxx
Fax xxxxx
derek.solano@pelhamrh.com
382 Wilmot Street Box 415
Harlow Mesa, Westland 76291

Font styles to use
Serif

Colors
f48340

Requirements
Must have
• Clean crisp lines and ability to modify names, titles and emails
• On the back "PelhamRidgeHospital.Com
Nice to have
• Needs to be in line with logo, which is a bit dated and not too appealing, but I'm hoping that the rest of the card can make up for that fact just a little bit.
• Hospital's colors are a copper brown, black and white
Should not have
• Shapes or anything distracting

```html
<!DOCTYPE html>
<html lang="en">
<head>
<meta charset="utf-8">
<title>Pelham Ridge Hospital – Business Card</title>
<link rel="stylesheet" href="https://fonts.googleapis.com/css2?family=Open+Sans:wght@400;600;700&display=swap">
<style>
  :root {
    --ink: #111111;
    --paper: #ffffff;
    --copper: #f48340;
    --stage: #d9d9d9;
    --muted: #222222;
  }
  html, body {
    margin: 0;
    padding: 0;
    width: 1200px;
    height: 900px;
    overflow: hidden;
    background: var(--stage);
    font-family: "Open Sans", Arial, sans-serif;
  }
  .canvas {
    position: relative;
    width: 1200px;
    height: 900px;
  }
  .card {
    position: absolute;
    width: 600px;
    height: 343px;
    box-shadow: 0 6px 18px rgba(0,0,0,0.25);
    overflow: hidden;
  }
  .card--back {
    left: 520px;
    top: 60px;
    background: var(--ink);
    color: var(--paper);
  }
  .card--back .brand {
    position: absolute;
    left: 0;
    right: 0;
    top: 120px;
    text-align: center;
    font-weight: 700;
    font-size: 34px;
    letter-spacing: 0.5px;
    color: var(--paper);
  }
  .card--back .web {
    position: absolute;
    left: 0;
    right: 0;
    bottom: 48px;
    text-align: center;
    font-size: 15px;
    letter-spacing: 1px;
  }
  .card--front {
    left: 80px;
    top: 480px;
    background: var(--paper);
    color: var(--ink);
  }
  .card--front .brand {
    position: absolute;
    left: 34px;
    top: 30px;
    font-weight: 700;
    font-size: 28px;
    color: var(--ink);
  }
  .contact {
    position: absolute;
    left: 34px;
    top: 88px;
    margin: 0;
    padding: 0;
    list-style: none;
    font-size: 13px;
    line-height: 20px;
    color: var(--muted);
  }
  .contact li {
    display: flex;
    align-items: center;
    gap: 8px;
    white-space: nowrap;
  }
  .contact .plain { padding-left: 22px; }
  .contact svg { width: 14px; height: 14px; flex: none; }
  .person {
    position: absolute;
    right: 60px;
    top: 168px;
  }
  .person__name {
    margin: 0;
    font-size: 24px;
    font-weight: 600;
    color: var(--copper);
  }
  .person__title {
    margin: 2px 0 0;
    font-size: 15px;
    color: var(--ink);
  }
  .footer-band {
    position: absolute;
    left: 0;
    bottom: 0;
    width: 600px;
    height: 120px;
  }
  .card--front .web {
    position: absolute;
    left: 0;
    right: 0;
    bottom: 16px;
    text-align: center;
    font-size: 16px;
    letter-spacing: 0.5px;
    color: var(--paper);
  }
</style>
</head>
<body>
<div class="canvas">

  <section class="card card--back" aria-label="Card back">
    <div class="brand">Pelham Ridge Hospital</div>
    <div class="web">www.PelhamRidgeHospital.Com</div>
  </section>

  <section class="card card--front" aria-label="Card front">
    <div class="brand">Pelham Ridge Hospital</div>

    <ul class="contact">
      <li class="plain">382 Wilmot St.</li>
      <li class="plain">Harlow Mesa, Westland 76291</li>
      <li>
        <svg viewBox="0 0 16 16" aria-hidden="true"><path fill="#f48340" d="M3.5 1.5l2.5 0 1 3.5-1.6 1.2a8 8 0 0 0 4.4 4.4L11 9l3.5 1v2.5c0 1-1 2-2 2A11 11 0 0 1 1.5 3.5c0-1 1-2 2-2z"/></svg>
        (555) 740-2386
      </li>
      <li>
        <svg viewBox="0 0 16 16" aria-hidden="true"><rect x="4" y="1" width="8" height="4" fill="#f48340"/><rect x="1" y="5" width="14" height="7" rx="1.5" fill="#f48340"/><rect x="4" y="10" width="8" height="5" fill="#fff" stroke="#f48340" stroke-width="1.2"/></svg>
        (555) 740-2390
      </li>
      <li>
        <svg viewBox="0 0 16 16" aria-hidden="true"><rect x="1" y="3" width="14" height="10" fill="#f48340"/><path d="M1 3.5l7 5 7-5" fill="none" stroke="#fff" stroke-width="1.3"/></svg>
        info@PelhamRidgeHospital.com
      </li>
    </ul>

    <div class="person">
      <p class="person__name">Elena Marquez</p>
      <p class="person__title">Doctor</p>
    </div>

    <svg class="footer-band" viewBox="0 0 600 120" preserveAspectRatio="none" aria-hidden="true">
      <path d="M0 20 C200 55 420 70 600 30 L600 120 L0 120 Z" fill="#f48340"/>
      <path d="M0 22 C200 60 420 82 600 48 L600 120 L0 120 Z" fill="#ffffff"/>
      <path d="M0 24 C200 66 420 92 600 58 L600 120 L0 120 Z" fill="#111111"/>
    </svg>
    <div class="web">www.PelhamRidgeHospital.Com</div>
  </section>

</div>
</body>
</html>
```